Photojournalism/photography business needs a simple, timeless & professional letterhead design

We need a letterhead design for photography/photojournalism business called 'plomk', no capitals.

The letterhead needs to be:
- simple
- professional
- timeless
- easy to read
- consists of at least 2 colors to make it stands out.

We do mainly editorial photography, photo articles for various publications, travel, businesses, as well as people such as family and kids.

The final design should communicate professionalism, easy identification, attention grabbing, even if it has to be found among a stack of various papers on the clients' desks.

Target Market(s)

Various publications.

Industry/Entity Type

Business

Requirements
Must have
• Please use the logo attached.

```html
<!DOCTYPE html>
<html lang="en">
<head>
<meta charset="utf-8">
<title>plomk letterhead</title>
<link href="https://fonts.googleapis.com/css2?family=Titillium+Web:wght@400;600;700&display=swap" rel="stylesheet">
<style>
  :root {
    --backdrop: #bfe2ef;
    --paper: #ffffff;
    --ribbon: #fdc33f;
    --ink: #333333;
    --footer: #3d3d3d;
    --footer-text: #ffffff;
  }
  * { margin: 0; padding: 0; box-sizing: border-box; }
  html, body {
    width: 1200px;
    height: 1000px;
    overflow: hidden;
    background: var(--backdrop);
    font-family: "Titillium Web", sans-serif;
  }
  .stage { position: relative; width: 1200px; height: 1000px; }
  .sheet {
    position: absolute;
    width: 336px;
    height: 475px;
    background: var(--paper);
  }
  .sheet--cover { left: 233px; top: 157px; }
  .sheet--letter { left: 616px; top: 262px; }
  .ribbon { position: absolute; top: 0; display: block; }
  .sheet--cover .ribbon { left: 204px; }
  .sheet--letter .ribbon { left: 58px; }
  .ribbon-shape { fill: var(--ribbon); }
  .brand-name {
    position: absolute;
    color: var(--ink);
    font-weight: 700;
    letter-spacing: 0.5px;
    line-height: 1;
    text-align: center;
  }
  .sheet--cover .brand-name { left: 204px; width: 81px; top: 178px; font-size: 26px; }
  .sheet--letter .brand-name { left: 58px; width: 82px; top: 34px; font-size: 24px; }
  .contact-bar {
    position: absolute;
    left: 0; bottom: 0;
    width: 336px;
    height: 22px;
    background: var(--footer);
    color: var(--footer-text);
    font-size: 6.5px;
    font-weight: 600;
  }
  .contact-item { position: absolute; top: 7px; white-space: nowrap; line-height: 1; }
  .contact-phone { left: 46px; }
  .contact-address { left: 119px; }
  .contact-web { left: 245px; }
</style>
</head>
<body>
<main class="stage">
  <section class="sheet sheet--cover" aria-label="Cover sheet">
    <svg class="ribbon" width="81" height="250" viewBox="0 0 81 250" aria-hidden="true">
      <polygon class="ribbon-shape" points="0,0 81,0 81,210 40.5,250 0,210"/>
    </svg>
    <div class="brand-name">plomk</div>
  </section>

  <section class="sheet sheet--letter" aria-label="Letterhead">
    <svg class="ribbon" width="82" height="105" viewBox="0 0 82 105" aria-hidden="true">
      <polygon class="ribbon-shape" points="0,0 82,0 82,63 41,105 0,63"/>
    </svg>
    <div class="brand-name">plomk</div>
    <footer class="contact-bar">
      <span class="contact-item contact-phone">+001 555 0142</span>
      <span class="contact-item contact-address">14 Harbor Lane, Port Vale 220417</span>
      <span class="contact-item contact-web">www.plomk.com</span>
    </footer>
  </section>
</main>
</body>
</html>
```